Modern Business Card for Industrial Company

We need business cards updated with modern fonts and make it look more technical, sharp and clean. The logo should not be changed, but we are looking for fresh solutions for how other information on the card is laid out in an interesting way. The company provides machinery and services to the ceramic industry and deals with cutting-edge technology. The design should reflect a technologically advanced and modern company that deals with the latest European technologies.

Font styles to use
Sans Serif

Requirements
Must have
• Modern fonts, technical look and feel

```html
<!DOCTYPE html>
<html lang="en">
<head>
<meta charset="utf-8">
<title>Korvant Technics – Business Card</title>
<link rel="stylesheet" href="https://fonts.googleapis.com/css2?family=Montserrat:wght@700&family=Roboto:wght@400;700&display=swap">
<style>
  :root {
    --backdrop: #8a8c8c;
    --card-white: #ffffff;
    --brand-blue: #0b5597;
    --brand-red: #b4202a;
    --text-grey: #5a5d61;
    --pattern-light: #8fa3d6;
    --pattern-dark: #1d5a9e;
  }
  * { margin: 0; padding: 0; box-sizing: border-box; }
  html, body {
    width: 1188px; height: 1200px; overflow: hidden;
    background: var(--backdrop);
    font-family: "Roboto", Arial, sans-serif;
  }
  .card {
    position: absolute; left: 245px; width: 696px; height: 386px;
  }
  .card--front { top: 159px; background: var(--card-white); }
  .card--back { top: 627px; background: var(--brand-blue); }

  .wordmark {
    position: absolute; left: 74px; top: 166px;
    display: flex; align-items: center; gap: 10px;
  }
  .wordmark__square { width: 14px; height: 14px; background: var(--brand-red); }
  .wordmark__name {
    font-family: "Roboto", Arial, sans-serif; font-weight: 700;
    font-size: 48px; letter-spacing: 1px; color: var(--brand-blue); line-height: 1;
  }

  .contact { position: absolute; left: 378px; top: 80px; color: var(--text-grey); }
  .contact__name {
    font-family: "Montserrat", Arial, sans-serif; font-weight: 700;
    font-size: 20px; color: var(--brand-blue); line-height: 1.2;
  }
  .contact__title { font-size: 18px; color: var(--brand-red); line-height: 1.3; }
  .contact__rule { width: 25px; height: 2px; background: var(--brand-blue); margin: 12px 0 13px; }
  .contact__company { font-size: 18px; color: var(--brand-blue); line-height: 23px; }
  .contact__address { font-size: 18px; line-height: 23px; }
  .contact__list { list-style: none; margin-top: 6px; }
  .contact__item {
    display: flex; align-items: center; gap: 7px;
    font-size: 18px; line-height: 25px;
  }
  .contact__icon { width: 18px; height: 18px; flex: none; }

  .back-pattern {
    position: absolute; left: 12px; top: 10px; right: 12px; bottom: 12px;
    background: linear-gradient(135deg, var(--pattern-light) 0%, #5f7cbf 40%, var(--pattern-dark) 100%);
    opacity: 0.55;
  }
  .back-wordmark {
    position: absolute; left: 468px; top: 265px;
    font-family: "Roboto", Arial, sans-serif; font-weight: 700;
    font-size: 34px; letter-spacing: 1px; color: var(--card-white); line-height: 1;
  }
</style>
</head>
<body>
  <section class="card card--front">
    <div class="wordmark">
      <span class="wordmark__square"></span>
      <span class="wordmark__name">KORVANT</span>
    </div>
    <div class="contact">
      <p class="contact__name">DARIO FERRETTI</p>
      <p class="contact__title">Director</p>
      <div class="contact__rule"></div>
      <p class="contact__company">Korvant Technics, Inc.</p>
      <p class="contact__address">418 Meridian Way, Suite 200<br>Fairhaven, GA 30112</p>
      <ul class="contact__list">
        <li class="contact__item">
          <svg class="contact__icon" viewBox="0 0 24 24"><path fill="#b4202a" d="M6.6 10.8c1.4 2.8 3.8 5.1 6.6 6.6l2.2-2.2c.3-.3.7-.4 1-.2 1.1.4 2.3.6 3.6.6.6 0 1 .4 1 1V20c0 .6-.4 1-1 1C10.6 21 3 13.4 3 4c0-.6.4-1 1-1h3.5c.6 0 1 .4 1 1 0 1.3.2 2.5.6 3.6.1.3 0 .7-.2 1l-2.3 2.2z"/></svg>
          (555) 014.2286
        </li>
        <li class="contact__item">
          <svg class="contact__icon" viewBox="0 0 24 24"><rect x="2" y="5" width="20" height="14" fill="#b4202a"/><path d="M2.5 5.5 12 13l9.5-7.5M2.5 18.5l7-6M21.5 18.5l-7-6" stroke="#fff" stroke-width="1.4" fill="none"/></svg>
          dferretti@korvant.com
        </li>
        <li class="contact__item">
          <svg class="contact__icon" viewBox="0 0 24 24" fill="none" stroke="#b4202a" stroke-width="1.8"><circle cx="12" cy="12" r="9.5"/><path d="M2.5 12h19M12 2.5c3 3 3 16 0 19M12 2.5c-3 3-3 16 0 19"/></svg>
          www.korvant.com
        </li>
      </ul>
    </div>
  </section>

  <section class="card card--back">
    <div class="back-pattern" role="img" aria-label="Repeating embossed brand-mark pattern in light-to-deep blue tones"></div>
    <span class="back-wordmark">KORVANT</span>
  </section>
</body>
</html>
```